Elegant and Professional Business card design needed

The client journey mentor is a company which provides consulting services to businesses to assist them in improving the customer experience for their customers.

I need a business card design which tells people I'm there to help them.

Target Market(s)

Small to medium business owners

Industry/Entity Type

Business

Contact Information for Business Card

Leonard Pashcroft
The Client Journey Mentor
Web: http://www.TheClientJourneyMentor.example
Email: leonard@TheClientJourneyMentor.example
Phone: +61 452 386017

Logo styles of interest
Abstract Logo
Requirements
Must have
• Some sort of image / graphic representing the customer is important and should be at the heart of a business.

```html
<!DOCTYPE html>
<html lang="en">
<head>
<meta charset="utf-8">
<title>The Client Journey Mentor – Business Card</title>
<link rel="stylesheet" href="https://fonts.googleapis.com/css2?family=PT+Sans:wght@700&family=PT+Sans+Narrow:wght@700&family=Source+Sans+3:wght@300;600&display=swap">
<style>
  :root {
    --card-bg: #f9edcf;
    --gold: #d4a040;
    --brown: #54493d;
    --badge: #efcb92;
  }
  html, body {
    margin: 0;
    padding: 0;
    overflow: hidden;
    background: var(--card-bg);
  }
  .card {
    position: relative;
    width: 1200px;
    height: 694px;
    background: var(--card-bg);
    overflow: hidden;
  }
  .company-name {
    position: absolute;
    left: 70px;
    top: 236px;
    margin: 0;
    font-family: "PT Sans", sans-serif;
    font-weight: 700;
    font-size: 58px;
    line-height: 1;
    color: var(--gold);
    letter-spacing: 0.2px;
  }
  .person-name {
    position: absolute;
    left: 70px;
    top: 346px;
    margin: 0;
    font-family: "PT Sans Narrow", sans-serif;
    font-weight: 700;
    font-size: 40px;
    line-height: 1;
    color: var(--brown);
  }
  .brand-mark {
    position: absolute;
    left: 880px;
    top: 96px;
    width: 220px;
    display: flex;
    flex-direction: column;
    align-items: flex-start;
    gap: 14px;
  }
  .brand-mark__dot {
    width: 40px;
    height: 40px;
    border-radius: 50%;
    background: var(--gold);
  }
  .brand-mark__name {
    font-family: "PT Sans", sans-serif;
    font-weight: 700;
    font-size: 30px;
    line-height: 1.1;
    color: var(--gold);
  }
  .contact-list {
    position: absolute;
    left: 332px;
    top: 443px;
    margin: 0;
    padding: 0;
    list-style: none;
  }
  .contact-item {
    display: flex;
    align-items: center;
    height: 58px;
    margin-bottom: 14px;
  }
  .contact-item__badge {
    width: 58px;
    height: 58px;
    border-radius: 50%;
    background: var(--badge);
    display: flex;
    align-items: center;
    justify-content: center;
    font-family: "Source Sans 3", sans-serif;
    font-weight: 600;
    font-size: 34px;
    line-height: 1;
    color: var(--brown);
    padding-bottom: 6px;
    box-sizing: border-box;
    flex: none;
  }
  .contact-item__text {
    margin-left: 20px;
    font-family: "Source Sans 3", sans-serif;
    font-weight: 300;
    font-size: 36px;
    color: var(--brown);
    white-space: nowrap;
  }
</style>
</head>
<body>
  <main class="card">
    <div class="brand-mark">
      <span class="brand-mark__dot"></span>
      <span class="brand-mark__name">The Client<br>Journey<br>Mentor</span>
    </div>

    <h1 class="company-name">The Client Journey Mentor</h1>
    <p class="person-name">Leonard Pashcroft</p>

    <ul class="contact-list">
      <li class="contact-item">
        <span class="contact-item__badge">w</span>
        <span class="contact-item__text">www.TheClientJourneyMentor.example</span>
      </li>
      <li class="contact-item">
        <span class="contact-item__badge">e</span>
        <span class="contact-item__text">leonard@TheClientJourneyMentor.example</span>
      </li>
      <li class="contact-item">
        <span class="contact-item__badge">p</span>
        <span class="contact-item__text">+61 452 386017</span>
      </li>
    </ul>
  </main>
</body>
</html>
```